Fresh, modern brand required for new start-up!

TallCedarRun is a new venture offering an end-to-end communications and media relations service including strategy development, execution and evaluation; copy writing and editing; social and e- media management; leadership coaching, media training and more.

I require a fresh and lively corporate identity to mirror the ethos of the business.

I need a logo, business card (double-sided preferably), letterhead (for invoicing and client communications) and compliment slip. As a start-up, budget will be an ongoing consideration for me so, ideally, I would prefer a two-colour logo - although if you wow me with something more than that, I may have to throw caution to the wind!

The ethos behind my name is twofold; one, I have moved from being something of a "big fish in a small pond" (a director in a single company) to a small fish in the big pond of small businesses. Two, I may be a "small fish", but that doesn't mean I don't "fish big".

I am looking for a clean, simple design that will look good on a variety of mediums, big or small. The design should be young and fresh and make an immediate impact. I want the design to reflect the fact that I specialise in tailored, simple and effective communications.

Target Market(s)

My clients range from global financial services, resources and technology companies to not-for-profit organisations and other small businesses. Moreover, my current client base stretches from Asia Pacific (incl. Australia), to Europe (incl. UK) and the US. All my clients speak English (even if as a second language) and are relatively senior communications professionals within their organisations.

Industry/Entity Type

Communications

Requirements
Nice to have
• The design/logo could include symbols and/or characters that double as imagery. For example: an upside down question mark (?) might look like a fishing line/hook and a flattened @ sign, might look like a pond...
Should not have
• The design should not use old-style serif fonts, but nor should it be "cartoony" in any way. No navy blue, grey or sombre corporate colours.

```html
<!DOCTYPE html>
<html lang="en">
<head>
<meta charset="utf-8">
<title>TallCedarRun — Stationery</title>
<link rel="stylesheet" href="https://fonts.googleapis.com/css2?family=Source+Sans+3:wght@400&display=swap">
<style>
  :root {
    --brand-blue: #45c8f3;
    --ink: #3f505c;
    --paper: #ffffff;
    --card-light: #f8f8f8;
    --card-dark: #e6e7e9;
    --shadow: rgba(0, 0, 0, 0.28);
  }
  * { margin: 0; padding: 0; box-sizing: border-box; }
  html, body { width: 1200px; height: 927px; overflow: hidden; background: var(--paper); }
  body { position: relative; font-family: "Source Sans 3", "Myriad Pro", Arial, sans-serif; color: var(--ink); }

  .mark { position: absolute; border-radius: 50%; background: var(--brand-blue); }
  .brand-name { position: absolute; white-space: nowrap; font-weight: 400; color: var(--ink); letter-spacing: 0.01em; line-height: 1; }

  .sheet {
    position: absolute;
    box-shadow: 2px 3px 6px var(--shadow);
  }
  .card { background: linear-gradient(160deg, var(--card-dark) 0%, var(--card-light) 70%, var(--paper) 100%); }
  .letterhead { background: var(--paper); }

  .contact-list { position: absolute; list-style: none; white-space: nowrap; }
  .contact-list li { position: relative; }
  .contact-list li::before {
    content: ""; position: absolute; left: -13px; top: 50%;
    width: 5px; height: 5px; border-radius: 50%; background: var(--brand-blue); transform: translateY(-50%);
  }

  .person { position: absolute; font-size: 13px; line-height: 1; white-space: nowrap; }
  .person .job-title { color: var(--brand-blue); }

  .slip-heading { position: absolute; font-size: 14px; line-height: 1; white-space: nowrap; }
</style>
</head>
<body>

  <!-- Primary brand lockup -->
  <section class="brand-lockup">
    <div class="mark" style="left:240px; top:112px; width:122px; height:122px;"></div>
    <div class="brand-name" style="left:304px; top:252px; font-size:44px; transform:translateX(-50%);">TallCedarRun</div>
  </section>

  <!-- Business card front -->
  <section class="sheet card card-front" style="left:113px; top:357px; width:383px; height:219px;">
    <div class="mark" style="left:155px; top:63px; width:72px; height:72px;"></div>
    <div class="brand-name" style="left:191px; top:150px; font-size:24px; transform:translateX(-50%);">TallCedarRun</div>
  </section>

  <!-- Business card back -->
  <section class="sheet card card-back" style="left:113px; top:611px; width:383px; height:218px;">
    <div class="mark" style="left:26px; top:38px; width:38px; height:38px;"></div>
    <div class="brand-name" style="left:69px; top:40px; font-size:21px;">TallCedarRun</div>
    <div class="person" style="left:70px; top:64px;">Name <span class="job-title">Job Title</span></div>
    <ul class="contact-list" style="left:258px; top:128px; font-size:11px; line-height:11.5px;">
      <li>+01 555-0142</li>
      <li>Fax 00 000 0000</li>
      <li>tallcedarrun@tcr.com</li>
      <li>Company Address</li>
      <li>www.tallcedarrun.com</li>
    </ul>
  </section>

  <!-- Letterhead -->
  <section class="sheet letterhead" style="left:558px; top:113px; width:555px; height:717px;">
    <div class="mark" style="left:250px; top:20px; width:48px; height:48px;"></div>
    <div class="brand-name" style="left:277px; top:78px; font-size:17px; transform:translateX(-50%);">TallCedarRun</div>
    <ul class="contact-list" style="left:253px; top:656px; font-size:8px; line-height:8px;">
      <li>+01 555-0142</li>
      <li>Fax 00 000 0000</li>
      <li>tallcedarrun@tcr.com</li>
      <li>Company Address</li>
      <li>www.tallcedarrun.com</li>
    </ul>
  </section>

  <!-- Compliment slip -->
  <section class="sheet card compliment-slip" style="left:577px; top:354px; width:516px; height:245px;">
    <div class="slip-heading" style="left:47px; top:32px;">With Compliments</div>
    <div class="mark" style="left:44px; top:164px; width:45px; height:45px;"></div>
    <div class="brand-name" style="left:24px; top:216px; font-size:16px;">TallCedarRun</div>
    <ul class="contact-list" style="left:410px; top:183px; font-size:10px; line-height:10px;">
      <li>+01 555-0142</li>
      <li>Fax 00 000 0000</li>
      <li>tallcedarrun@tcr.com</li>
      <li>Company Address</li>
      <li>www.tallcedarrun.com</li>
    </ul>
  </section>

</body>
</html>
```